HVAC Contractor Website Design

We are working with an HVAC contractor in Idaho called QR HVAC.
Some sites to use for content/competitors and inspiration:
https://www.brindlevent.example
https://plumcrest.example/web/contractor/ (lots of contractor website designs we've approved and continue to show clients)
Thank you for taking the time to consider designing a website for us. We are web developers based in Stockton, CA, USA. Most of our projects go through the same process. Understanding this process may help you win a project with us. We custom-code all of our websites in-house. We don’t have any requirements as to what tools you use for your design, but we prefer Figma files. For any design that we label as four-stars, we send it to the client for review. The client picks the final design they want us to use. Once we complete this process, we will continue to show additional clients all the four-star sites and purchase them later. Your designs will have multiple chances to sell. For better chances of success, we ask that you follow these guidelines.
IMAGES:
If you use any images or icons in the design, we ask that you have a link to the asset so we can purchase the image/icon. Most of the designs we submit do not have the customer’s images on them unless they have some great images. Be creative; show us the feeling you are trying to portray with your image choices. Use any royalty-free site you choose. We subscribe to Velmora and mainly use their images, but we can purchase images outside of Velmora.
PLEASE NOTE: we will not submit designs to clients with watermarks on the images.
FONTS:
We ask that you identify the fonts used in the design. This can be done in a message if you want. We typically use Google Fonts and Velmora Fonts.
CONTENT:
We're always open to different content and ideas. We often submit designs with stock images so the client can see our vision. We typically take pictures after the website launch to use their images with our vision. Lorem Ipsum is fine for paragraphs, but we ask that you write the headers in correct English. We want to be able to show the vision and identify the sections of the website.
INSPIRATION:
We typically add a couple of links in the brief of websites we like to help you get started in your design.
REVISIONS:
We do not often ask for revisions of the designs unless we see something in the design that may not appeal to the client. If there are slight changes that we want to make, we do that in the development process.
FEEDBACK:
We rarely give feedback on designs during the design process. We are working on many website projects and do not have the time to provide feedback. We usually respond if your request is well thought out and asks specific questions, but a note asking “feedback, please” usually goes unanswered
Number of Pages Required
1 page
Look and feel
Each slider illustrates characteristics of the customer's brand and the style your logo design should communicate.

```html
<!DOCTYPE html>
<html lang="en">
<head>
<meta charset="utf-8">
<title>QR HVAC – Cooling &amp; Heating</title>
<link rel="stylesheet" href="https://fonts.googleapis.com/css2?family=Poppins:wght@400;500;600;700;800;900&display=swap">
<style>
:root{
  --blue:#0a3fa8;
  --blue-deep:#0b2f8f;
  --sky:#14b4f0;
  --red:#f4200e;
  --orange:#ff7a00;
  --yellow:#ffb300;
  --ink:#111111;
  --grey:#6b6b6b;
  --white:#ffffff;
  --dark:#0f1115;
}
*{margin:0;padding:0;box-sizing:border-box}
html,body{width:1200px;height:4223px;overflow:hidden}
body{font-family:"Poppins",sans-serif;background:var(--white);color:var(--ink);position:relative}
.abs{position:absolute}
.btn{position:absolute;display:flex;align-items:center;justify-content:center;border-radius:22px;color:var(--white);font-weight:700;font-size:13px;letter-spacing:.2px;text-transform:uppercase}
.btn-warm{background:linear-gradient(90deg,var(--yellow),var(--red))}
.btn-cool{background:linear-gradient(90deg,var(--sky),var(--blue-deep))}
.btn-sky{background:var(--sky)}
.photo{position:absolute}

/* header */
.brand{position:absolute;display:flex;align-items:center;gap:12px;font-weight:800;font-size:46px;color:var(--blue-deep);letter-spacing:-1px}
.brand-dot{width:26px;height:26px;border-radius:50%;background:var(--sky)}
.contact{position:absolute;display:flex;align-items:center;gap:16px}
.contact-icon{width:48px;height:48px;border-radius:50%;background:linear-gradient(135deg,var(--sky),var(--blue-deep));display:flex;align-items:center;justify-content:center}
.contact small{display:block;font-size:10px;color:var(--grey)}
.contact strong{display:block;font-size:17px;font-weight:600;color:var(--ink)}
.nav{position:absolute;left:361px;top:90px;width:839px;height:50px;background:var(--red)}
.nav-home{position:absolute;left:361px;top:90px;width:131px;height:50px;background:var(--yellow);clip-path:polygon(28px 0,100% 0,100% 100%,0 100%)}
.nav ul{list-style:none;display:flex;position:absolute;left:0;top:0;height:50px;align-items:center;font-size:14px;color:var(--white);font-weight:500}
.nav li{position:absolute;white-space:nowrap}

/* hero */
.hero-photo{left:0;top:140px;width:1200px;height:540px;background:linear-gradient(100deg,#3a2a1f 0%,#5b4736 35%,#7d8a8f 60%,#4f6a3a 100%)}
.hero-shade{left:0;top:140px;width:1200px;height:540px;background:linear-gradient(90deg,rgba(0,0,0,.55),rgba(0,0,0,0) 60%)}
.hero h2{position:absolute;left:111px;top:242px;color:var(--white);font-size:32px;font-weight:700}
.hero h1{position:absolute;left:106px;top:282px;color:var(--white);font-size:84px;font-weight:800;letter-spacing:-1px}
.hero p{position:absolute;left:111px;top:396px;width:480px;color:var(--white);font-size:17px;line-height:33px;font-weight:500}

/* about & maintenance */
.section-title{position:absolute;font-size:45px;font-weight:800;color:var(--ink);line-height:58px;letter-spacing:.5px}
.body-copy{position:absolute;font-size:16px;line-height:31px;color:var(--grey)}
.body-copy p+p{margin-top:13px}

/* cooling / heating */
.split h3{position:absolute;color:var(--white);font-weight:700;font-size:24px;display:flex;align-items:center;justify-content:center}
.split .lead{position:absolute;color:var(--white);font-size:16px;line-height:31px}
.ticks{position:absolute;list-style:none;color:var(--white);font-size:16px;line-height:31px}
.ticks li{position:relative;padding-left:32px}
.ticks li::before{content:"";position:absolute;left:0;top:7px;width:17px;height:17px;border-radius:50%;background:var(--white)}
.ticks li::after{content:"";position:absolute;left:4px;top:14px;width:8px;height:3px;background:var(--ink)}

/* provide */
.centered{position:absolute;left:0;width:1200px;text-align:center}
.card{position:absolute;top:2177px;width:318px;height:426px;background:var(--white);box-shadow:0 8px 30px rgba(0,0,0,.08)}
.card-photo{position:absolute;left:0;top:0;width:318px;height:223px;clip-path:polygon(0 0,100% 0,100% 100%,0 88%)}
.card h4{position:absolute;left:29px;top:235px;font-size:20px;font-weight:600}
.card p{position:absolute;left:29px;top:275px;width:265px;font-size:12.5px;line-height:26px;color:var(--grey)}
.card .btn{left:27px;top:364px;width:116px;height:35px;font-size:12px}
.slider-arrow{position:absolute;top:2378px;width:24px;height:24px;border-radius:50%;display:flex;align-items:center;justify-content:center}

/* cta */
.cta h2{font-size:45px;font-weight:800;color:var(--white);letter-spacing:1px}
.cta p{color:var(--white);font-size:16px;line-height:31px}
.cta .contact small,.cta .contact strong{color:var(--white)}

/* footer */
.footer-nav{position:absolute;top:4089px;left:0;width:1200px;font-size:14px;color:var(--white);font-weight:500}
.footer-nav span{position:absolute;transform:translateX(-50%);white-space:nowrap}
.social{position:absolute;top:4133px;width:32px;height:32px;border-radius:50%;background:linear-gradient(135deg,var(--yellow),var(--red))}
</style>
</head>
<body>

<!-- Header -->
<header>
  <div class="brand" style="left:82px;top:36px"><span class="brand-dot"></span>QR HVAC</div>
  <div class="contact" style="left:569px;top:22px">
    <span class="contact-icon"><svg width="20" height="20" viewBox="0 0 24 24"><path fill="#fff" d="M6.6 10.8a15 15 0 0 0 6.6 6.6l2.2-2.2a1 1 0 0 1 1-.25 11.4 11.4 0 0 0 3.6.57 1 1 0 0 1 1 1V20a1 1 0 0 1-1 1A17 17 0 0 1 3 4a1 1 0 0 1 1-1h3.5a1 1 0 0 1 1 1c0 1.25.2 2.45.57 3.57a1 1 0 0 1-.25 1z"/></svg></span>
    <div><small>Call Us:</small><strong>+1 555 010 0199</strong></div>
  </div>
  <div class="contact" style="left:810px;top:22px">
    <span class="contact-icon"><svg width="20" height="20" viewBox="0 0 24 24"><path fill="#fff" d="M3 6h18v12H3z"/><path fill="none" stroke="#0a3fa8" stroke-width="1.6" d="M3 6l9 7 9-7"/></svg></span>
    <div><small>Email Us:</small><strong>info@qrhvacadmin.com</strong></div>
  </div>
  <nav class="nav">
    <ul>
      <li style="left:58px">Home</li>
      <li style="left:171px">About Us</li>
      <li style="left:286px">Our Services</li>
      <li style="left:425px">Testimonials</li>
      <li style="left:567px">Blog</li>
      <li style="left:650px">Contact Us</li>
    </ul>
  </nav>
  <div class="nav-home"></div>
  <div class="abs" style="left:418px;top:104px;color:#fff;font-size:14px;font-weight:500">Home</div>
</header>

<!-- Hero -->
<section class="hero">
  <div class="photo hero-photo" role="img" aria-label="Two outdoor air conditioning condenser units beside a house with green plants"></div>
  <div class="abs hero-shade"></div>
  <h2>WELCOME TO</h2>
  <h1>QR HVAC</h1>
  <p>Lorem ipsum dolor sit amet, consectetur adipiscing elit, sed do eiusmod tempor incididunt ut labore</p>
  <a class="btn btn-warm" style="left:111px;top:488px;width:140px;height:42px">Get Started</a>
  <svg class="abs" style="left:0;top:580px" width="1200" height="102" viewBox="0 0 1200 102">
    <path d="M0 102 L600 10 L1200 102 Z" fill="#fff"/>
    <path d="M0 100 L600 4 L1200 90 L1200 102 L600 20 Z" fill="#0b2f8f"/>
    <path d="M60 102 L600 16 L1140 102 L1200 102 L600 24 L0 102Z" fill="#fff"/>
    <path d="M600 0 L760 22 L600 16 L440 22Z" fill="#14b4f0"/>
  </svg>
</section>

<!-- About -->
<section class="about">
  <div class="photo" style="left:111px;top:737px;width:392px;height:427px;border-radius:6px;background:linear-gradient(160deg,#5b6c86,#3c3a36 60%,#8a8a80)" role="img" aria-label="Technician in hard hat servicing an outdoor air conditioning unit"></div>
  <div class="photo" style="left:360px;top:936px;width:227px;height:279px;border-radius:8px;background:linear-gradient(160deg,#2c4a7a,#9aa3a8 60%,#d5d8d6);box-shadow:0 10px 25px rgba(0,0,0,.2)" role="img" aria-label="Close-up of a technician testing electrical wiring inside a unit"></div>
  <h2 class="section-title" style="left:651px;top:806px">ABOUT US</h2>
  <div class="body-copy" style="left:651px;top:873px;width:450px">
    <p>Sed ut perspiciatis unde omnis iste natus error sit voluptatem accusantium doloremque laudantium, totam rem aperiam, eaque ipsa quae ab illo inventore veritatis et quasi architecto</p>
    <p>Nemo enim ipsam voluptatem quia volu ptas sit as-pernatur aut odit aut fugit</p>
  </div>
  <a class="btn btn-cool" style="left:651px;top:1093px;width:140px;height:40px">Read More</a>
</section>

<!-- Cooling / Heating -->
<section class="split">
  <svg class="abs" style="left:0;top:1287px" width="1200" height="660" viewBox="0 0 1200 660">
    <defs>
      <linearGradient id="coolGrad" x1="0" y1="0" x2="1" y2="1"><stop offset="0" stop-color="#12b2ef"/><stop offset="1" stop-color="#0b2f8f"/></linearGradient>
      <linearGradient id="warmGrad" x1="0" y1="0" x2="1" y2="1"><stop offset="0" stop-color="#ffb300"/><stop offset=".55" stop-color="#ff6a00"/><stop offset="1" stop-color="#f4200e"/></linearGradient>
    </defs>
    <polygon points="525,0 1200,0 1200,603 640,603" fill="url(#warmGrad)"/>
    <polygon points="0,37 545,37 672,659 0,659" fill="url(#coolGrad)"/>
  </svg>
  <h3 style="left:251px;top:1419px;width:314px;height:73px;background:var(--red);clip-path:polygon(0 0,100% 0,100% 100%,16px 100%)">HVAC COOLING</h3>
  <h3 style="left:541px;top:1370px;width:319px;height:76px;background:var(--blue-deep);clip-path:polygon(0 0,96% 0,100% 100%,16px 100%)">HVAC HEATIING</h3>
  <p class="lead" style="left:108px;top:1520px;width:430px">Lorem ipsum dolor sit amet, consectetur adipiscing elit, sed do eiusmod tempor incididunt ut labore et dolore magna aliqua.</p>
  <ul class="ticks" style="left:141px;top:1627px;width:400px">
    <li>Lorem ipsum dolor sit amet, consectetur adipiscing elit</li>
    <li>Sed do eiusmod tempor incididunt ut</li>
    <li>Quis ipsum suspendisse u ltrices gravi da.</li>
    <li>Risus commodo viverra maecenas</li>
  </ul>
  <a class="btn btn-sky" style="left:108px;top:1811px;width:143px;height:40px">Get Started</a>
  <p class="lead" style="left:675px;top:1475px;width:420px">Lorem ipsum dolor sit amet, consectetur adipiscing elit, sed do eiusmod tempor incididunt ut labore et dolore magna aliqua.</p>
  <ul class="ticks" style="left:707px;top:1582px;width:400px">
    <li>Lorem ipsum dolor sit amet, consectetur adipiscing elit</li>
    <li>Sed do eiusmod tempor incididunt ut</li>
    <li>Quis ipsum suspendisse u ltrices gravi da.</li>
    <li>Risus commodo viverra maecenas</li>
  </ul>
  <a class="btn" style="left:675px;top:1766px;width:143px;height:40px;background:var(--red)">Get Started</a>
</section>

<!-- What we provide -->
<section class="provide">
  <h2 class="centered" style="top:2017px;font-size:45px;font-weight:800">WHAT WE PROVIDE</h2>
  <p class="centered" style="top:2085px;font-size:16px;line-height:31px;color:var(--grey)">Lorem ipsum dolor sit amet, consectetur adipiscing elit, sed do eiusmod tempor incididunt ut labore et<br>dolore magna aliqua. Ut enim ad minim veniam, quis nostrud exercitation ullamco laboris nisi</p>
  <span class="slider-arrow" style="left:49px;background:#c9c9c9"><svg width="12" height="12" viewBox="0 0 12 12"><path d="M8 2 4 6l4 4" fill="none" stroke="#fff" stroke-width="2"/></svg></span>
  <span class="slider-arrow" style="left:1127px;background:#333"><svg width="12" height="12" viewBox="0 0 12 12"><path d="M4 2l4 4-4 4" fill="none" stroke="#fff" stroke-width="2"/></svg></span>

  <article class="card" style="left:103px">
    <div class="card-photo" style="background:linear-gradient(135deg,#a4553f,#c9745a 50%,#8d4735)" role="img" aria-label="Technician on a ladder installing a wall air conditioner while a customer watches"></div>
    <h4>Air Conditioning</h4>
    <p>Lorem ipsum dolor sit amet, consectetur adipiscing elit, sed do eiusmod tempor inci didunt ut labore et dolore</p>
    <a class="btn btn-cool">Read More</a>
  </article>
  <article class="card" style="left:441px">
    <div class="card-photo" style="background:linear-gradient(135deg,#e9e3dc,#c9bcae 60%,#b7a795)" role="img" aria-label="Family relaxing on a sofa beneath a wall-mounted air conditioner"></div>
    <h4>Indoor Air Quality</h4>
    <p>Lorem ipsum dolor sit amet, consectetur adipiscing elit, sed do eiusmod tempor inci didunt ut labore et dolore</p>
    <a class="btn btn-cool">Read More</a>
  </article>
  <article class="card" style="left:779px">
    <div class="card-photo" style="background:linear-gradient(135deg,#d9dcdf,#8f9aa0 50%,#6f9a45)" role="img" aria-label="Technician in red uniform servicing an outdoor heat pump on a lawn"></div>
    <h4>Heat Pumps</h4>
    <p>Lorem ipsum dolor sit amet, consectetur adipiscing elit, sed do eiusmod tempor inci didunt ut labore et dolore</p>
    <a class="btn btn-cool">Read More</a>
  </article>
</section>

<!-- Work with us -->
<section class="cta">
  <div class="photo" style="left:0;top:2688px;width:1200px;height:492px;background:linear-gradient(180deg,#0b3aa8,#0a2f8c)" role="img" aria-label="Row of outdoor air conditioning units tinted deep blue"></div>
  <svg class="abs" style="left:0;top:2688px" width="1200" height="492" viewBox="0 0 1200 492">
    <path d="M0 0 L1200 0 L600 60 Z" fill="#fff"/>
    <path d="M60 0 L600 50 L1140 0 L1200 0 L600 62 L0 0Z" fill="#14b4f0"/>
    <path d="M0 492 L600 420 L1200 492 Z" fill="#fff"/>
    <path d="M60 492 L600 412 L1140 492 L1200 492 L600 424 L0 492Z" fill="#14b4f0"/>
  </svg>
  <h2 class="centered" style="top:2828px">WANT TO WORK WITH US</h2>
  <p class="centered" style="top:2898px">Lorem ipsum dolor sit amet, consectetur adipiscing elit, sed do eiusmod tempor incididunt ut labore et dolore<br>magna aliqua. Ut enim ad minim veniam, quis nostrud exercitation ullamco laboris nisi</p>
  <div class="contact" style="left:361px;top:2993px">
    <span class="contact-icon" style="background:var(--sky)"><svg width="20" height="20" viewBox="0 0 24 24"><path fill="#fff" d="M6.6 10.8a15 15 0 0 0 6.6 6.6l2.2-2.2a1 1 0 0 1 1-.25 11.4 11.4 0 0 0 3.6.57 1 1 0 0 1 1 1V20a1 1 0 0 1-1 1A17 17 0 0 1 3 4a1 1 0 0 1 1-1h3.5a1 1 0 0 1 1 1c0 1.25.2 2.45.57 3.57a1 1 0 0 1-.25 1z"/></svg></span>
    <div><small>Call Us:</small><strong>+1 555 010 0199</strong></div>
  </div>
  <div class="contact" style="left:629px;top:2993px">
    <span class="contact-icon" style="background:var(--sky)"><svg width="20" height="20" viewBox="0 0 24 24"><path fill="#fff" d="M3 6h18v12H3z"/><path fill="none" stroke="#14b4f0" stroke-width="1.6" d="M3 6l9 7 9-7"/></svg></span>
    <div><small>Email Us:</small><strong>info@qrhvacadmin.com</strong></div>
  </div>
</section>

<!-- Maintenance -->
<section class="maintenance">
  <div class="abs" style="left:287px;top:3262px;width:226px;height:70px;background:linear-gradient(90deg,var(--yellow),var(--orange));clip-path:polygon(12% 0,100% 0,88% 100%,0 100%)"></div>
  <div class="abs" style="left:184px;top:3686px;width:222px;height:68px;background:linear-gradient(90deg,var(--orange),var(--red));clip-path:polygon(12% 0,100% 0,88% 100%,0 100%)"></div>
  <div class="photo" style="left:111px;top:3327px;width:474px;height:364px;background:linear-gradient(135deg,#c9b896,#8a6a5a 45%,#a8332f 70%,#4a5a86)" role="img" aria-label="Smiling technician giving a thumbs up beside pipes and a yellow toolbox"></div>
  <h2 class="section-title" style="left:651px;top:3308px">MAINTENANCE &amp;<br>INSTALLING</h2>
  <div class="body-copy" style="left:651px;top:3438px;width:450px">
    <p>Sed ut perspiciatis unde omnis iste natus error sit voluptatem accusantium doloremque laudantium, totam rem aperiam, eaque ipsa quae ab illo inventore veritatis et quasi architecto</p>
    <p>Nemo enim ipsam voluptatem quia volu ptas sit as pernatur aut odit aut fugit</p>
  </div>
  <a class="btn btn-cool" style="left:651px;top:3655px;width:140px;height:41px">Read More</a>
</section>

<!-- Footer -->
<footer>
  <div class="photo" style="left:0;top:3824px;width:1200px;height:399px;background:linear-gradient(180deg,#15181d,#0b0d10)" role="img" aria-label="Dark view of rooftop air conditioning units"></div>
  <svg class="abs" style="left:0;top:3824px" width="1200" height="70" viewBox="0 0 1200 70">
    <path d="M0 0 L1200 0 L600 60 Z" fill="#fff"/>
    <path d="M60 0 L600 50 L1140 0 L1200 0 L600 64 L0 0Z" fill="#0b3aa8"/>
  </svg>
  <div class="brand" style="left:470px;top:3995px;color:var(--white)"><span class="brand-dot"></span>QR HVAC</div>
  <div class="footer-nav">
    <span style="left:286px">Home</span>
    <span style="left:409px">About Us</span>
    <span style="left:537px">Our Services</span>
    <span style="left:677px">Testimonials</span>
    <span style="left:790px">Blog</span>
    <span style="left:896px">Contact Us</span>
  </div>
  <span class="social" style="left:540px"></span>
  <span class="social" style="left:585px"></span>
  <span class="social" style="left:629px"></span>
  <p class="centered" style="top:4183px;font-size:12px;color:var(--white)">(C) Copyright 2024 | All Rights Reserved</p>
</footer>

</body>
</html>
```